Start up Dialysis Clinic needs its first website - Velmora Health

Create a visually appealing and user-friendly website for Velmora Health, a dialysis clinic located in Mt. Irvine, Tobago. The website should effectively communicate our services to local, regional, and international patients, providing essential information and fostering trust and engagement..
Key Goals:

1. Informative: Provide comprehensive information about our services, facility, and team.
2. User-Friendly: Ensure the website is easy to navigate, with a clear structure and accessible content.
3. Engaging: Create a visually appealing design that reflects the professionalism and care of Velmora Health.
4. Responsive: Ensure the website is fully responsive and performs well on all devices, including desktops, tablets, and smartphones.
5. Trust-Building: Include testimonials, credentials, and patient resources to build trust with potential patients.
Scope of Work:

1. Home Page: An inviting and informative landing page that provides an overview of our clinic, mission, and services. Include a call to action for more information and contact details.
2. About Us: A detailed page about Velmora Health, including our mission, vision, team, and facility tour.
3. Services: A comprehensive page describing the dialysis services we offer, including Hemodialysis, Peritoneal Dialysis, and Home Hemodialysis.
4. Patient Information: A resourceful section with guides for new patients, FAQs, insurance and billing information, and downloadable forms.
5. Resources: Educational content about kidney health, dialysis options, diet and nutrition tips, and support groups.
6. Contact Us: A contact page with our address, phone number, email, office hours, a contact form, and a map.

```html
<!DOCTYPE html>
<html lang="en">
<head>
<meta charset="utf-8">
<title>Velmora Health – Dialysis Clinic</title>
<link href="https://fonts.googleapis.com/css2?family=Barlow+Condensed:wght@500;600;700&family=Roboto:wght@400;500&display=swap" rel="stylesheet">
<style>
:root{
  --green:#6aa343;
  --blue:#1f6fbe;
  --band-blue:#4a7fc2;
  --ink:#111;
  --text:#333;
  --muted:#777;
  --white:#fff;
  --footer:#000;
  --head:"Barlow Condensed", sans-serif;
  --body:"Roboto", sans-serif;
}
*{box-sizing:border-box;margin:0;padding:0}
html,body{width:1200px;height:4029px;overflow:hidden}
body{position:relative;background:var(--white);font-family:var(--body);color:var(--text)}
.abs{position:absolute}
.head{font-family:var(--head);text-transform:uppercase}

/* header */
.topline{left:0;top:0;width:1200px;height:3px;background:linear-gradient(90deg,var(--green),var(--blue))}
.brand{left:131px;top:30px;display:flex;align-items:center;gap:10px;font-family:var(--head);font-weight:700;font-size:28px;color:var(--blue);letter-spacing:.5px}
.brand .mark{width:24px;height:24px;background:var(--green)}
.icon-dot{width:40px;height:40px;border-radius:50%;display:flex;align-items:center;justify-content:center}
.call-label{left:433px;top:28px;font-family:var(--head);font-weight:600;font-size:17px;color:var(--ink)}
.call-num{left:433px;top:48px;font-family:var(--head);font-weight:600;font-size:24px;color:var(--green);letter-spacing:.3px}
.addr{left:688px;top:30px;font-size:13.5px;line-height:20px;color:var(--muted);width:220px}
.btn{display:flex;align-items:center;justify-content:center;font-family:var(--head);font-weight:600;text-transform:uppercase;color:var(--white);letter-spacing:.4px}
.consult{left:915px;top:27px;width:174px;height:37px;border-radius:20px;background:var(--green);font-size:15px}
.nav{left:470px;top:100px;width:570px;height:42px}
.nav ul{position:absolute;left:0;top:0;width:100%;list-style:none;font-size:15px;color:var(--text)}
.nav li{position:absolute;top:2px;white-space:nowrap}
.nav li.active{color:var(--green)}

/* hero */
.hero{left:0;top:110px;width:1200px;height:586px;background:linear-gradient(100deg,#5a5550 0%,#8b7d6c 25%,#c9b59a 42%,#d6d3cd 62%,#b9bec4 80%,#8e949a 100%)}
.welcome{left:110px;top:277px;width:133px;height:28px;background:var(--green);font-size:18px}
.hero-title{left:106px;top:310px;font-family:var(--head);font-weight:700;font-size:92px;line-height:82px;color:var(--white)}
.hero-line{left:0;top:526px;width:128px;height:2px;background:var(--blue)}
.play{left:127px;top:502px;width:44px;height:44px;border-radius:50%;background:var(--blue);border:3px solid var(--green);display:flex;align-items:center;justify-content:center}

/* about */
.about-frame{left:74px;top:785px;width:359px;height:413px;border:1.5px solid var(--blue)}
.about-photo{left:113px;top:821px;width:388px;height:402px;background:linear-gradient(135deg,#2f7a5e,#3d8e6f 40%,#c9d6d8 70%,#6c8a93);border:5px solid var(--green)}
.eyebrow{font-family:var(--head);font-weight:600;font-size:20px;color:var(--green);text-transform:uppercase}
.h2{font-family:var(--head);font-weight:600;font-size:38px;color:var(--ink);text-transform:uppercase;line-height:1}
.para{font-size:15.3px;line-height:30px;color:var(--text)}
.btn-green{background:var(--green);border-radius:5px;font-size:18px}
.btn-blue{background:var(--blue);border-radius:5px;font-size:18px}

/* services */
.svc{top:1469px;width:299px;height:349px}
.svc-label{position:absolute;left:0;width:100%;text-align:center;font-family:var(--head);font-weight:600;font-size:21px;color:var(--white);text-transform:uppercase}
.svc-mid{left:451px;top:1469px;width:298px;height:401px;background:var(--green);color:var(--white);text-align:center}
.svc-mid h3{position:absolute;top:70px;width:100%;font-family:var(--head);font-weight:600;font-size:27px}
.svc-mid p{position:absolute;top:119px;left:20px;width:258px;font-size:14px;line-height:25.6px}
.svc-mid a{position:absolute;top:326px;left:0;width:100%;font-family:var(--head);font-size:16px;color:#cfe5bf;text-decoration:underline}
.arrow{width:34px;height:34px;border-radius:50%;display:flex;align-items:center;justify-content:center}

/* testimonials */
.band{left:0;top:1993px;width:1200px;height:491px;background:var(--band-blue)}
.t-card{top:2156px;height:217px;background:var(--white);border-radius:4px;overflow:hidden}
.avatar{position:absolute;left:22px;top:17px;width:50px;height:50px;border-radius:50%;background:linear-gradient(135deg,#c9906b,#5a4030)}
.t-name{position:absolute;left:95px;top:25px;font-family:var(--head);font-weight:600;font-size:18px;color:var(--ink)}
.t-date{position:absolute;left:97px;top:49px;font-size:12px;color:var(--muted)}
.t-text{position:absolute;left:98px;top:76px;width:440px;font-size:12.2px;line-height:27px;color:#222;white-space:nowrap;overflow:hidden}
.stars{position:absolute;left:98px;top:164px;display:flex;gap:4px}
.progress{left:280px;top:2434px;width:648px;height:5px;border-radius:3px;background:#f1f1f1}
.progress span{position:absolute;left:153px;top:0;width:88px;height:5px;background:var(--green)}

/* mission */
.circle-green{left:932px;top:2570px;width:194px;height:194px;border-radius:50%;background:var(--green)}
.circle-blue{left:535px;top:2835px;width:370px;height:370px;border-radius:50%;background:#e3eff9}
.mission-photo{left:673px;top:2639px;width:386px;height:463px;border-radius:14px;background:linear-gradient(160deg,#e9ecee,#cfd6da 40%,#4fa0b8 70%,#7a3a4a)}

/* footer */
.footer{left:0;top:3325px;width:1200px;height:704px;background:var(--footer);color:var(--white)}
.foot-brand{left:0;top:3475px;width:1200px;display:flex;justify-content:center;align-items:center;gap:14px;font-family:var(--head);font-weight:700;font-size:52px;color:var(--blue);letter-spacing:1px}
.foot-brand .mark{width:40px;height:40px;background:var(--green)}
.foot-h{top:3662px;font-family:var(--head);font-weight:600;font-size:21px;color:var(--white)}
.foot-h::after{content:"";position:absolute;left:0;top:33px;width:26px;height:2px;background:#555}
.foot-list{font-size:14.5px;color:var(--white);list-style:none}
.foot-list li{position:absolute;white-space:nowrap;display:flex;align-items:center;gap:9px}
.field{left:845px;width:244px;border-bottom:1.5px solid #888;font-size:14px;color:#ccc;padding-bottom:6px}
.submit{left:845px;top:3835px;width:127px;height:39px;border-radius:20px;background:var(--green);font-size:11px}
.copy{left:0;top:3980px;width:1200px;text-align:center;font-size:14.5px;color:var(--white)}
</style>
</head>
<body>

<div class="abs topline"></div>

<header>
  <div class="abs brand"><span class="mark"></span>VELMORA HEALTH</div>

  <div class="abs icon-dot" style="left:377px;top:25px;background:var(--blue)">
    <svg width="18" height="18" viewBox="0 0 24 24"><path fill="#fff" d="M6.6 10.8a15.1 15.1 0 0 0 6.6 6.6l2.2-2.2c.3-.3.7-.4 1-.2 1.1.4 2.3.6 3.6.6.6 0 1 .4 1 1V20c0 .6-.4 1-1 1A17 17 0 0 1 3 4c0-.6.4-1 1-1h3.5c.6 0 1 .4 1 1 0 1.3.2 2.5.6 3.6.1.3 0 .7-.2 1z"/></svg>
  </div>
  <div class="abs call-label">CALL US</div>
  <div class="abs call-num">+1 868 555 0142</div>

  <div class="abs icon-dot" style="left:634px;top:27px;background:var(--green)">
    <svg width="16" height="18" viewBox="0 0 24 24"><path fill="#fff" d="M12 2a7 7 0 0 0-7 7c0 5.3 7 13 7 13s7-7.7 7-13a7 7 0 0 0-7-7zm0 9.5A2.5 2.5 0 1 1 12 6.5a2.5 2.5 0 0 1 0 5z"/></svg>
  </div>
  <div class="abs addr">12b Lorem ipsum dolor sit amet, consectetur adipiscing</div>

  <div class="abs btn consult">Free Consultation</div>
</header>

<section class="abs hero" role="img" aria-label="Smiling patient seated while a doctor writes on a clipboard in a bright clinic room"></section>

<nav class="abs nav">
  <svg class="abs" style="left:0;top:10px" width="570" height="32" viewBox="0 0 570 32"><polygon points="0,0 570,0 540,32 28,32" fill="#fff"/></svg>
  <ul>
    <li class="active" style="left:44px">Home</li>
    <li style="left:119px">About</li>
    <li style="left:193px">Services</li>
    <li style="left:284px">Patient</li>
    <li style="left:366px">Resources</li>
    <li style="left:471px">Contact</li>
  </ul>
</nav>

<div class="abs btn welcome">Welcome to</div>
<h1 class="abs hero-title">VELMORA<br>HEALTH</h1>
<div class="abs hero-line"></div>
<div class="abs play"><svg width="14" height="14" viewBox="0 0 10 10"><polygon points="2,1 9,5 2,9" fill="#fff"/></svg></div>

<!-- about -->
<section>
  <div class="abs about-frame"></div>
  <div class="abs about-photo" role="img" aria-label="Doctor in a white coat consulting with a patient at a desk"></div>
  <div class="abs eyebrow" style="left:549px;top:796px">Our Clinic</div>
  <h2 class="abs h2" style="left:549px;top:832px">About Velmora Health</h2>
  <p class="abs para" style="left:554px;top:878px;width:540px">Lorem ipsum dolor sit amet, consectetur adipiscing elit, sed do eiusmod tempor incididunt ut labore et dolore magna aliqua. Quis ipsum sus­pendisse ultrices gravida. Risus commodo viverra maecenas accumsan lacus vel facilisis.</p>
  <p class="abs para" style="left:554px;top:1028px;width:540px">Lorem ipsum dolor sit amet, consectetur adipiscing elit, sed do eiusmod tempor incididunt ut labore et dolore magna aliqua. Quis ipsum sus­pendisse ultrices gravida. Risus commodo viverra maecenas accumsan lacus vel facilisis.</p>
  <div class="abs btn btn-green" style="left:552px;top:1170px;width:160px;height:53px">Leran More</div>
</section>

<!-- services -->
<section>
  <div class="abs eyebrow" style="left:0;top:1346px;width:1200px;text-align:center">Services</div>
  <h2 class="abs h2" style="left:0;top:1381px;width:1200px;text-align:center">Our Services</h2>

  <div class="abs arrow" style="left:83px;top:1605px;background:var(--blue)"><svg width="10" height="10" viewBox="0 0 10 10"><polyline points="6,2 3,5 6,8" fill="none" stroke="#fff" stroke-width="1.5"/></svg></div>
  <div class="abs arrow" style="left:1092px;top:1605px;background:var(--green)"><svg width="10" height="10" viewBox="0 0 10 10"><polyline points="4,2 7,5 4,8" fill="none" stroke="#fff" stroke-width="1.5"/></svg></div>

  <div class="abs svc" style="left:147px;background:linear-gradient(135deg,#d8d8d4,#9ea4aa 50%,#4e5a6a)" role="img" aria-label="Doctor explaining treatment to a patient">
    <div class="svc-label" style="top:296px">Hemodialysis</div>
  </div>
  <div class="abs svc-mid">
    <h3>PERITONEAL DIALYSIS</h3>
    <p>Lorem ipsum dolor sit amet, consec­tetur adipiscing elit, sed do eiusmod tempor incididunt ut labore et dolore magna aliqua. Quis ipsum suspendisse ultrices gravida. Risus commodo viverra maecenas ac­cumsan lacus vel facilisis.</p>
    <a>LEARN MORE</a>
  </div>
  <div class="abs svc" style="left:753px;background:linear-gradient(135deg,#6a5548,#3e3a3a 50%,#2a2c30)" role="img" aria-label="Patient filling in a form on a clipboard at home">
    <div class="svc-label" style="top:289px">Home Hemodialysis.</div>
  </div>
</section>

<!-- testimonials -->
<section>
  <div class="abs band" role="img" aria-label="Faded group of smiling clinic members behind a blue overlay"></div>
  <div class="abs head" style="left:0;top:2049px;width:1200px;text-align:center;font-size:14px;color:#8fc46a">Client Testimonials</div>
  <h2 class="abs h2" style="left:0;top:2078px;width:1200px;text-align:center;color:var(--white)">What Our Members Say</h2>

  <article class="abs t-card" style="left:113px;width:563px">
    <div class="avatar" role="img" aria-label="Member portrait"></div>
    <div class="t-name">MARCUS DELANEY</div>
    <div class="t-date">2024-02-27</div>
    <p class="t-text">Lorem ipsum dolor sit amet, consectetur adipiscing elit, sed do eiusmod<br>tempor incididunt ut labore et dolore magna aliqua. Quis ipsum suspendisse<br>ultrices gravida. Risus commodo viverra maecenas accumsan lacus vel</p>
    <div class="stars">
      <svg width="58" height="10" viewBox="0 0 58 10"><g fill="#f3a712"><polygon points="5,0 6.2,3.6 10,3.6 7,5.9 8.1,9.5 5,7.3 1.9,9.5 3,5.9 0,3.6 3.8,3.6"/><polygon transform="translate(12 0)" points="5,0 6.2,3.6 10,3.6 7,5.9 8.1,9.5 5,7.3 1.9,9.5 3,5.9 0,3.6 3.8,3.6"/><polygon transform="translate(24 0)" points="5,0 6.2,3.6 10,3.6 7,5.9 8.1,9.5 5,7.3 1.9,9.5 3,5.9 0,3.6 3.8,3.6"/><polygon transform="translate(36 0)" points="5,0 6.2,3.6 10,3.6 7,5.9 8.1,9.5 5,7.3 1.9,9.5 3,5.9 0,3.6 3.8,3.6"/><polygon transform="translate(48 0)" points="5,0 6.2,3.6 10,3.6 7,5.9 8.1,9.5 5,7.3 1.9,9.5 3,5.9 0,3.6 3.8,3.6"/></g></svg>
    </div>
  </article>
  <article class="abs t-card" style="left:738px;width:462px;border-radius:4px 0 0 4px">
    <div class="avatar" role="img" aria-label="Member portrait"></div>
    <div class="t-name">MARCUS DELANEY</div>
    <div class="t-date">2024-02-27</div>
    <p class="t-text" style="width:364px">Lorem ipsum dolor sit amet, consectetur adipiscing elit, sed do eiusmod<br>tempor incididunt ut labore et dolore magna aliqua. Quis ipsum suspendisse<br>ultrices gravida. Risus commodo viverra maecenas accumsan lacus vel</p>
    <div class="stars">
      <svg width="58" height="10" viewBox="0 0 58 10"><g fill="#f3a712"><polygon points="5,0 6.2,3.6 10,3.6 7,5.9 8.1,9.5 5,7.3 1.9,9.5 3,5.9 0,3.6 3.8,3.6"/><polygon transform="translate(12 0)" points="5,0 6.2,3.6 10,3.6 7,5.9 8.1,9.5 5,7.3 1.9,9.5 3,5.9 0,3.6 3.8,3.6"/><polygon transform="translate(24 0)" points="5,0 6.2,3.6 10,3.6 7,5.9 8.1,9.5 5,7.3 1.9,9.5 3,5.9 0,3.6 3.8,3.6"/><polygon transform="translate(36 0)" points="5,0 6.2,3.6 10,3.6 7,5.9 8.1,9.5 5,7.3 1.9,9.5 3,5.9 0,3.6 3.8,3.6"/><polygon transform="translate(48 0)" points="5,0 6.2,3.6 10,3.6 7,5.9 8.1,9.5 5,7.3 1.9,9.5 3,5.9 0,3.6 3.8,3.6"/></g></svg>
    </div>
  </article>
  <div class="abs progress"><span></span></div>
</section>

<!-- mission -->
<section>
  <div class="abs circle-green"></div>
  <div class="abs circle-blue"></div>
  <div class="abs mission-photo" role="img" aria-label="Doctor with stethoscope writing notes at a desk"></div>
  <div class="abs eyebrow" style="left:88px;top:2684px">Velmora Health</div>
  <h2 class="abs h2" style="left:87px;top:2717px">Our Mission</h2>
  <p class="abs para" style="left:91px;top:2774px;width:540px">Lorem ipsum dolor sit amet, consectetur adipiscing elit, sed do eiusmod tempor incididunt ut labore et dolore magna aliqua. Quis ipsum sus­pendisse ultrices gravida. Risus commodo viverra maecenas accumsan lacus vel facilisis.&nbsp; Lorem ipsum dolor sit amet, consectetur adipiscing elit, sed do eiusmod tempor incididunt ut labore et dolore magna aliqua. Quis ipsum suspendisse ultrices gravida. Risus commodo viverra maece­nas accumsan lacus vel facilisis. Lorem ipsum dolor sit amet, consectetur adipiscing elit, sed do eiusmod tempor incididunt</p>
  <div class="abs btn btn-blue" style="left:89px;top:3033px;width:160px;height:55px">Leran More</div>
</section>

<!-- footer -->
<footer>
  <div class="abs footer"></div>
  <div class="abs foot-brand"><span class="mark"></span>VELMORA HEALTH</div>

  <div class="abs foot-h" style="left:111px">CONTACT US</div>
  <div class="abs foot-h" style="left:374px">HELP LINK</div>
  <div class="abs foot-h" style="left:623px">FOLLOW US</div>
  <div class="abs foot-h" style="left:842px">SIGNUP TO NEWSLETTER</div>

  <ul class="foot-list">
    <li style="left:114px;top:3721px;align-items:flex-start"><svg width="10" height="14" viewBox="0 0 24 24"><path fill="var(--blue)" d="M12 2a7 7 0 0 0-7 7c0 5.3 7 13 7 13s7-7.7 7-13a7 7 0 0 0-7-7z"/></svg><span style="line-height:25px;margin-top:-5px">12b Velmora health dolor<br>sit amet</span></li>
    <li style="left:114px;top:3785px"><svg width="12" height="12" viewBox="0 0 24 24"><path fill="var(--blue)" d="M6.6 10.8a15.1 15.1 0 0 0 6.6 6.6l2.2-2.2c.3-.3.7-.4 1-.2 1.1.4 2.3.6 3.6.6.6 0 1 .4 1 1V20c0 .6-.4 1-1 1A17 17 0 0 1 3 4c0-.6.4-1 1-1h3.5c.6 0 1 .4 1 1 0 1.3.2 2.5.6 3.6.1.3 0 .7-.2 1z"/></svg>+1 868 555 0142</li>
    <li style="left:114px;top:3823px"><svg width="14" height="10" viewBox="0 0 14 10"><rect width="14" height="10" fill="var(--blue)"/><polyline points="0,0 7,6 14,0" fill="none" stroke="#000" stroke-width="1"/></svg>hello@velmorahealth.com</li>
    <li style="left:114px;top:3856px;align-items:flex-start"><svg width="13" height="13" viewBox="0 0 14 14"><circle cx="7" cy="7" r="6" fill="none" stroke="var(--blue)" stroke-width="1.5"/><polyline points="7,3.5 7,7 9.5,8.5" fill="none" stroke="var(--blue)" stroke-width="1.5"/></svg><span style="font-size:12px;line-height:17px;margin-top:-1px"><b style="font-family:var(--head);font-size:14px">OFFICE HOURS</b><br>Mon-Friday<br>8am-6pm</span></li>
  </ul>

  <ul class="foot-list">
    <li style="left:376px;top:3722px"><svg width="6" height="10" viewBox="0 0 6 10"><polyline points="1,1 5,5 1,9" fill="none" stroke="#fff" stroke-width="1.4"/></svg>Terms &amp; Condtions</li>
    <li style="left:376px;top:3752px"><svg width="6" height="10" viewBox="0 0 6 10"><polyline points="1,1 5,5 1,9" fill="none" stroke="#fff" stroke-width="1.4"/></svg>Privacy Policy</li>
    <li style="left:376px;top:3782px"><svg width="6" height="10" viewBox="0 0 6 10"><polyline points="1,1 5,5 1,9" fill="none" stroke="#fff" stroke-width="1.4"/></svg>About Us</li>
    <li style="left:376px;top:3812px"><svg width="6" height="10" viewBox="0 0 6 10"><polyline points="1,1 5,5 1,9" fill="none" stroke="#fff" stroke-width="1.4"/></svg>Support</li>
  </ul>

  <ul class="foot-list">
    <li style="left:626px;top:3719px"><svg width="10" height="10"><circle cx="5" cy="5" r="4" fill="#fff"/></svg>Linkwave</li>
    <li style="left:626px;top:3749px"><svg width="10" height="10"><circle cx="5" cy="5" r="4" fill="#fff"/></svg>Snapfold</li>
    <li style="left:626px;top:3779px"><svg width="10" height="10"><circle cx="5" cy="5" r="4" fill="#fff"/></svg>Chirpline</li>
    <li style="left:626px;top:3809px"><svg width="10" height="10"><circle cx="5" cy="5" r="4" fill="#fff"/></svg>Cliptok</li>
  </ul>

  <div class="abs field" style="top:3719px">Name*</div>
  <div class="abs field" style="top:3771px">Email*</div>
  <div class="abs btn submit">Submit Now</div>

  <div class="abs copy">©Copyrights 2024&nbsp; Velmora health.&nbsp; |&nbsp;&nbsp;&nbsp; All Rights Reserved</div>
</footer>

</body>
</html>
```